Integrative Medical Practice Website Redo

I am needing to have our current website redesigned to make it a responsive website to work on smartphones.
Current website
www.brightoakfm.com
Here are several examples of what I am looking for
https://www.corvanhealth.com/
I am wanting a popup for a newsletter signup
Looking for a very professional, clean, simple, minimalist, bold well designed website
Colors would ideally be greens and blues, cool tones, muted colors, or graytones like:
https://journeybright.org/
Several other clean design examples
http://7harborsrenton.com/
http://www.belvomedical.com/
http://sunpathyouth.com/
http://yourcellduke.com/
I would like the top navigation bar to be able to slide down while browsing site
We are also needing to add several features that are not on our current website:
Questionnaire buttons
Are you toxic questionnaire?
Take our hormone quiz to find out if hormones are affecting your health.
online scheduling option for:
nutrition counselling
testing like body composition, basal metabolic rate, CIMT, breast thermography, VO2 Max testing, Vita Trace
Therapies like whole body vibration, infrared sauna, Exercise with oxygen, hyperbaric oxygen, spinal decompression
Need to have separate page for different services and split up services into:
Consults/Office Visits, Testing, Therapies, Procedures
Need to have a button link to patient portal
Needs to have online store
Need to add navigation button "Start Here"
Need a spot for a video on practice summary
Newsletter signup to collect emails
Testimonials from linkpage
Blog that posts can be shared with social media
Password protected patient access that can integrate into crate.net ideally
Modules for programs online classes/videos
I have attached stock images that you can use, but feel free to find others to use.
I have also attached a copy of our current brochure that shows an overview of the practice
Target Market(s)
Health conscious people of all ages looking for a family medicine doctor
Industry/Entity Type
Alternative Medicine
Coding
Coded - Design and coding required
Number of Pages Required
5+ page
Look and feel

```html
<!DOCTYPE html>
<html lang="en">
<head>
<meta charset="utf-8">
<title>Bright Oak Family Medicine</title>
<link href="https://fonts.googleapis.com/css2?family=Roboto:wght@400;500;700&family=Roboto+Slab:wght@400;700&display=swap" rel="stylesheet">
<style>
:root{
  --green:#8dc257;
  --green-dark:#7ab043;
  --blue:#5ba4cf;
  --text:#555;
  --muted:#888;
  --heading:#444;
  --light:#f4f4f4;
  --white:#fff;
  --dark:#3a3a3a;
}
*{box-sizing:border-box;margin:0;padding:0}
html,body{width:1200px;height:3579px;overflow:hidden}
body{font-family:'Roboto',sans-serif;color:var(--text);background:var(--white);font-size:13px;line-height:1.9}
.wrap{width:1028px;margin:0 auto;position:relative}
.slab{font-family:'Roboto Slab',serif}

/* header */
.site-header{height:91px}
.site-header .wrap{display:flex;justify-content:space-between;align-items:center;height:91px}
.brand{display:flex;align-items:center;gap:12px}
.brand-dot{width:34px;height:34px;border-radius:50%;background:var(--blue)}
.brand-name{font-family:'Roboto Slab',serif;font-weight:700;font-size:34px;color:var(--blue);line-height:1}
.socials{display:flex;gap:10px}
.socials span{width:38px;height:38px;border:2px solid #bbb;border-radius:50%;display:block}

.main-nav{height:52px;background:var(--green)}
.main-nav ul{list-style:none;display:flex;height:52px}
.main-nav li{color:#fff;font-size:12px;font-weight:500;text-transform:uppercase;padding:0 22px;line-height:52px}
.main-nav li.active{background:var(--blue)}

/* hero */
.hero{height:442px;position:relative;background:linear-gradient(100deg,#c9a890 0%,#e2cbb7 40%,#ead8c8 70%,#d8bca4 100%)}
.hero-box{position:absolute;left:91px;top:148px;width:410px;height:217px;background:rgba(70,60,55,.55);padding:22px 24px;color:#fff}
.hero-box .kicker{font-family:'Roboto Slab',serif;font-size:23px;line-height:1.2}
.hero-box h1{font-family:'Roboto Slab',serif;font-weight:400;font-size:36px;color:#b9e07f;line-height:1.3;margin-bottom:10px}
.hero-box p{font-size:11.5px;line-height:1.9}
.dots{position:absolute;right:22px;bottom:12px;display:flex;gap:5px}
.dots i{width:7px;height:7px;border-radius:50%;background:#fff;display:block}
.dots i.on{background:var(--green)}

/* welcome */
.welcome{height:513px;text-align:center;padding-top:36px}
.welcome h2{font-family:'Roboto Slab',serif;font-weight:400;font-size:27px;color:var(--heading)}
.welcome .tag{font-family:'Roboto Slab',serif;color:var(--green);font-size:15px;margin-top:12px}
.welcome .intro{width:820px;margin:14px auto 0;font-size:11.5px;color:var(--muted);line-height:2.1}
.features{display:flex;justify-content:space-between;margin-top:46px}
.feature{width:300px}
.feature .icon{width:114px;height:114px;border-radius:50%;margin:0 auto;display:flex;align-items:center;justify-content:center;border:4px solid #fff;box-shadow:0 0 0 3px currentColor}
.feature .icon.g{background:var(--green);color:var(--green)}
.feature .icon.b{background:var(--blue);color:var(--blue)}
.feature h3{font-size:15px;font-weight:700;text-transform:uppercase;margin-top:22px}
.feature h3.g{color:var(--green)}.feature h3.b{color:var(--blue)}
.feature p{font-size:11.5px;color:var(--muted);line-height:2.1;margin-top:6px}

/* services */
.services{height:382px;background:var(--light);padding-top:35px}
.services .wrap{display:flex;justify-content:space-between}
.service{width:241px;text-align:center}
.service .photo{height:196px}
.service h3{font-size:15px;font-weight:700;color:var(--green);text-transform:uppercase;margin-top:16px}
.service p{font-size:11.5px;color:var(--muted);line-height:1.75}

/* cta band */
.cta{height:124px;background:var(--green)}
.cta .wrap{display:flex;justify-content:space-between;align-items:center;height:124px;padding:0 44px}
.cta p{font-family:'Roboto Slab',serif;font-weight:700;color:#fff;font-size:22px}
.btn-outline{border:2px solid #fff;color:#fff;font-size:13px;font-weight:500;padding:7px 30px;text-transform:uppercase;border-radius:3px}

/* programs */
.programs{height:381px;background:linear-gradient(90deg,#3d3734 0%,#5a4f49 50%,#6b6058 100%);color:#fff}
.programs .wrap{display:flex;justify-content:space-between;padding-top:40px}
.programs .copy{width:570px}
.programs h2{font-family:'Roboto Slab',serif;font-weight:400;font-size:24px;text-transform:uppercase}
.programs h2 em{font-style:normal;color:#b9e07f}
.programs p{font-size:11.5px;line-height:2.2;margin-top:16px}
.btn{display:inline-block;background:var(--green);color:#fff;font-size:12px;font-weight:500;text-transform:uppercase;padding:6px 18px;border-radius:3px}
.programs .btn{margin-top:24px}
.video{position:relative;display:flex;align-items:center;justify-content:center}
.programs .video{width:484px;height:275px;margin-top:22px;background:linear-gradient(180deg,#9fc7ea 0%,#d9e9f5 60%,#9cc06a 85%,#7fa852 100%)}
.play{width:70px;height:70px;border-radius:50%;background:rgba(255,255,255,.92);display:flex;align-items:center;justify-content:center}

/* newsletter */
.newsletter{height:270px;text-align:center;padding-top:46px}
.section-title{font-family:'Roboto Slab',serif;font-weight:400;font-size:20px;color:var(--green);text-transform:uppercase}
.newsletter p{width:680px;margin:16px auto 0;font-size:11.5px;color:var(--text);line-height:2.1}
.signup{display:flex;width:632px;height:50px;margin:20px auto 0}
.signup .field{flex:1;background:#f1f1f1;border:1px solid #e3e3e3;text-align:left;padding:0 14px;line-height:48px;font-size:11px;color:#999}
.signup .submit{width:150px;background:var(--green);color:#fff;font-weight:700;font-size:13px;line-height:50px;text-transform:uppercase}

/* blog */
.blog{height:620px;background:var(--light);text-align:center;padding-top:32px}
.blog .sub{font-size:11.5px;color:var(--text);margin-top:4px}
.cards{display:flex;justify-content:space-between;margin-top:24px}
.card{width:334px;height:463px;background:#fff;border:1px solid #e6e6e6;position:relative}
.card .photo{height:222px;position:relative}
.card .photo:after{content:"";position:absolute;left:50%;bottom:0;margin-left:-10px;border:10px solid transparent;border-bottom-color:#fff}
.card h3{font-size:15px;font-weight:700;color:var(--green);text-transform:uppercase;margin-top:22px}
.card .date{font-size:11px;color:var(--text)}
.card .excerpt{font-size:11.5px;color:var(--text);line-height:2.1;padding:0 26px;margin-top:22px}
.card .meta{position:absolute;left:0;right:0;bottom:0;height:58px;border-top:1px solid #eee;margin:0 18px;display:flex;justify-content:space-between;align-items:center;font-size:11px;color:#777}
.card .meta .counts{display:flex;gap:12px;align-items:center}
.card .meta .counts span{display:flex;gap:4px;align-items:center}
.card .meta .more{color:var(--green);font-weight:700;text-transform:uppercase}

/* practice summary */
.summary{height:389px}
.summary .wrap{display:flex;justify-content:space-between;padding-top:43px}
.summary .video{width:482px;height:310px;background:linear-gradient(135deg,#2a2a2a 0%,#7a4a2c 55%,#b06d3c 100%)}
.summary .copy{width:470px;padding-top:14px}
.summary h2{font-family:'Roboto Slab',serif;font-weight:400;font-size:20px;color:var(--green);text-transform:uppercase}
.summary p{font-size:11.5px;line-height:2.3;margin-top:10px}
.summary .btn{margin-top:18px}

/* footer */
.site-footer{height:248px;background:#f3f3f3}
.site-footer .wrap{display:flex;padding-top:34px}
.foot-brand{width:312px;padding-top:48px;display:flex;gap:12px;align-items:center;align-self:flex-start}
.foot-col h4{font-size:14px;font-weight:700;color:var(--heading);text-transform:uppercase;margin-bottom:12px}
.contact{width:284px}
.contact li,.links li{list-style:none;font-size:11px;line-height:2.35;display:flex;align-items:center;gap:10px}
.contact a{color:var(--text)}
.links{width:220px}
.links li:before{content:"";width:0;height:0;border:4px solid transparent;border-left-color:#999;margin-right:4px}
.follow{width:212px}
.follow p{font-size:10.5px;line-height:1.8;margin-bottom:12px}
.follow .socials span{width:32px;height:32px}
.bottom-bar{height:67px;background:var(--green);color:#fff;text-align:center;font-size:11.5px;line-height:67px}
</style>
</head>
<body>

<header class="site-header">
  <div class="wrap">
    <div class="brand"><span class="brand-dot"></span><span class="brand-name">Bright Oak</span></div>
    <div class="socials"><span></span><span></span><span></span><span></span><span></span></div>
  </div>
</header>

<nav class="main-nav">
  <div class="wrap">
    <ul>
      <li class="active">Home</li><li>About Us</li><li>Services</li><li>Resources</li><li>FAQ</li><li>Patients</li><li>New Patients</li><li>Membership</li><li>Contact Us</li>
    </ul>
  </div>
</nav>

<section class="hero" role="img" aria-label="Woman smiling while receiving a shoulder massage">
  <div class="hero-box">
    <div class="kicker">WELL BEING</div>
    <h1>FAMILY MEDICINE</h1>
    <p>Welcome to our website. As an integrative medical practice, we provide innovative, quality family health care by uniquely combining both conventional and alternative medicine</p>
    <div class="dots"><i class="on"></i><i></i><i></i></div>
  </div>
</section>

<section class="welcome">
  <div class="wrap">
    <h2>Welcome to Bright Oak</h2>
    <p class="tag">Restoring your Health Naturally with Nutrition, Manipulation, Acupuncture, &amp; Integrative Medicine</p>
    <p class="intro">Welcome to our website. As an integrative medical practice, we provide innovative, quality family health care by uniquely combining both conventional and alternative medicine. Our aim is to treat the whole patient not just the symptoms. This "best of both worlds" approach provides patients with options in the management of their concerns while addressing</p>
    <div class="features">
      <div class="feature">
        <div class="icon g"><svg width="54" height="64" viewBox="0 0 54 64" fill="none" stroke="#fff" stroke-width="4" stroke-linecap="round"><circle cx="27" cy="8" r="6" fill="#fff" stroke="none"/><path d="M27 16v24M27 40l-9 20M27 40l9 20M10 30l17-8 17 8"/><circle cx="8" cy="30" r="4"/><circle cx="46" cy="30" r="4"/></svg></div>
        <h3 class="g">Exercise with Oxygen</h3>
        <p>Welcome to our website. As an integrative medical practice, we provide innovative, quality family health care by uniquely combining</p>
      </div>
      <div class="feature">
        <div class="icon b"><svg width="60" height="60" viewBox="0 0 60 60" fill="none" stroke="#fff" stroke-width="4"><circle cx="30" cy="30" r="7" fill="#fff"/><circle cx="12" cy="12" r="6"/><circle cx="48" cy="12" r="6"/><circle cx="30" cy="52" r="6"/><path d="M16 16l9 9M44 16l-9 9M30 37v9"/></svg></div>
        <h3 class="b">Hyperbaric Oxygen</h3>
        <p>Welcome to our website. As an integrative medical practice, we provide innovative, quality family health care by uniquely combining</p>
      </div>
      <div class="feature">
        <div class="icon g"><svg width="62" height="62" viewBox="0 0 62 62" fill="none" stroke="#fff" stroke-width="4"><circle cx="31" cy="31" r="18"/><circle cx="31" cy="31" r="6" fill="#fff"/><path d="M31 2v14M31 46v14M2 31h14M46 31h14"/></svg></div>
        <h3 class="g">Breast Thermography</h3>
        <p>Welcome to our website. As an integrative medical practice, we provide innovative, quality family health care by uniquely combining</p>
      </div>
    </div>
  </div>
</section>

<section class="services">
  <div class="wrap">
    <div class="service">
      <div class="photo" role="img" aria-label="Smiling mother with two children" style="background:linear-gradient(135deg,#e8c9a4,#d9a87a 50%,#7fb0c9)"></div>
      <h3>Family Medicine</h3>
      <p>In addition to what you would expect from any family medicine clinic, we utilize many different modalities in our</p>
    </div>
    <div class="service">
      <div class="photo" role="img" aria-label="Hands performing a back manipulation" style="background:linear-gradient(135deg,#f0e6de,#c98e6a 55%,#9a5d3e)"></div>
      <h3>Manipulation</h3>
      <p>In addition to what you would expect from any family medicine clinic, we utilize many different modalities in our</p>
    </div>
    <div class="service">
      <div class="photo" role="img" aria-label="Fresh berries and fruit" style="background:linear-gradient(135deg,#2a2230,#4a2a3a 50%,#a4303c)"></div>
      <h3>Nutrition</h3>
      <p>In addition to what you would expect from any family medicine clinic, we utilize many different modalities in our</p>
    </div>
    <div class="service">
      <div class="photo" role="img" aria-label="Acupuncture needle held over skin" style="background:linear-gradient(135deg,#a8471e,#d57a3a 55%,#e9b47c)"></div>
      <h3>Acupuncture</h3>
      <p>In addition to what you would expect from any family medicine clinic, we utilize many different modalities in our</p>
    </div>
  </div>
</section>

<section class="cta">
  <div class="wrap">
    <p>Welcome to our website. As an integrative medical practice</p>
    <span class="btn-outline">Online Store</span>
  </div>
</section>

<section class="programs" role="img" aria-label="Muted background photo of a relaxed woman">
  <div class="wrap">
    <div class="copy">
      <h2>Programs <em>Online Classes</em></h2>
      <p>At the heart of this practice, though, is the partnership between doctor and patient in the process of healing. Our staff is dedicated to providing high-quality, individualized and compassionate care to patients of all ages We aim to thoroughly educate you about</p>
      <p>At the heart of this practice, though, is the partnership between doctor and patient in the process of healing. Our staff is dedicated to providing high-quality, individualized and compassionate care to patients of all ages We aim to thoroughly educate you about</p>
      <span class="btn">Read More</span>
    </div>
    <div class="video" role="img" aria-label="Video of a woman with open arms in a sunny field">
      <span class="play"><svg width="26" height="28" viewBox="0 0 26 28"><path d="M4 2l20 12L4 26z" fill="var(--green)"/></svg></span>
    </div>
  </div>
</section>

<section class="newsletter">
  <div class="wrap">
    <h2 class="section-title">Subscribe to our Newsletter</h2>
    <p>This website is just one of the many ways we hope to teach and inspire you towards embracing your full health potential. As you navigate through the site, you will find a wealth of information about our practice</p>
    <div class="signup"><span class="field">Enter Your Email Id :</span><span class="submit">Subscribe</span></div>
  </div>
</section>

<section class="blog">
  <div class="wrap">
    <h2 class="section-title">Latest Blog</h2>
    <p class="sub">This website is just one of the many ways we hope to teach and inspire you towards embracing</p>
    <div class="cards">
      <article class="card">
        <div class="photo" role="img" aria-label="Happy couple outdoors" style="background:linear-gradient(160deg,#9cc7e6,#dcbfa0 60%,#c89a72)"></div>
        <h3>Approach Provides</h3>
        <div class="date">26 DECEMBER 2016</div>
        <p class="excerpt">Patients with options in the management of their concerns while addressing the underlying their illness. And as a primary care practice</p>
        <div class="meta"><div class="counts"><span><svg width="12" height="12" viewBox="0 0 12 12"><path d="M1 1h10v7H5l-3 3V8H1z" fill="none" stroke="#888"/></svg>5</span><span><svg width="12" height="11" viewBox="0 0 12 11"><path d="M6 10L1 5a2.6 2.6 0 0 1 5-3 2.6 2.6 0 0 1 5 3z" fill="none" stroke="#888"/></svg>4</span></div><span class="more">Read More</span></div>
      </article>
      <article class="card">
        <div class="photo" role="img" aria-label="Massage therapy on a shoulder" style="background:linear-gradient(160deg,#5a3a28,#b27a52 55%,#e6c7a8)"></div>
        <h3>Approach Provides</h3>
        <div class="date">26 DECEMBER 2016</div>
        <p class="excerpt">Patients with options in the management of their concerns while addressing the underlying their illness. And as a primary care practice</p>
        <div class="meta"><div class="counts"><span><svg width="12" height="12" viewBox="0 0 12 12"><path d="M1 1h10v7H5l-3 3V8H1z" fill="none" stroke="#888"/></svg>5</span><span><svg width="12" height="11" viewBox="0 0 12 11"><path d="M6 10L1 5a2.6 2.6 0 0 1 5-3 2.6 2.6 0 0 1 5 3z" fill="none" stroke="#888"/></svg>4</span></div><span class="more">Read More</span></div>
      </article>
      <article class="card">
        <div class="photo" role="img" aria-label="Close-up of blueberries" style="background:linear-gradient(160deg,#1c2a3c,#3a5a80 55%,#7f9bbf)"></div>
        <h3>Approach Provides</h3>
        <div class="date">26 DECEMBER 2016</div>
        <p class="excerpt">Patients with options in the management of their concerns while addressing the underlying their illness. And as a primary care practice</p>
        <div class="meta"><div class="counts"><span><svg width="12" height="12" viewBox="0 0 12 12"><path d="M1 1h10v7H5l-3 3V8H1z" fill="none" stroke="#888"/></svg>5</span><span><svg width="12" height="11" viewBox="0 0 12 11"><path d="M6 10L1 5a2.6 2.6 0 0 1 5-3 2.6 2.6 0 0 1 5 3z" fill="none" stroke="#888"/></svg>4</span></div><span class="more">Read More</span></div>
      </article>
    </div>
  </div>
</section>

<section class="summary">
  <div class="wrap">
    <div class="video" role="img" aria-label="Video of acupuncture needles on a back">
      <span class="play"><svg width="26" height="28" viewBox="0 0 26 28"><path d="M4 2l20 12L4 26z" fill="var(--green)"/></svg></span>
    </div>
    <div class="copy">
      <h2>Practice Summary</h2>
      <p>In our practice, we believe prevention is the key to lifelong health and wellness. We are committed to helping you get well, stay well and live well. It is our mission not only to heal, but to motivate patients</p>
      <p>At the heart of this practice, though, is the partnership between doctor &amp; patient in the process of healing. Our staff is dedicated to providing high- individualized and compassionate patients of all ages</p>
      <span class="btn">Read More</span>
    </div>
  </div>
</section>

<footer class="site-footer">
  <div class="wrap">
    <div class="foot-brand"><span class="brand-dot"></span><span class="brand-name">Bright Oak</span></div>
    <div class="foot-col contact">
      <h4>Contact Us</h4>
      <ul>
        <li><svg width="12" height="12" viewBox="0 0 12 12"><path d="M2 1h3l1 3-2 1a7 7 0 0 0 3 3l1-2 3 1v3c-5 1-10-4-9-9z" fill="#888"/></svg>(000)-123-1231 (Phone)</li>
        <li><svg width="12" height="12" viewBox="0 0 12 12"><rect x="1" y="4" width="10" height="7" fill="#888"/><rect x="3" y="1" width="6" height="3" fill="#888"/></svg>(000)-123-1231 (Fax)</li>
        <li><svg width="12" height="12" viewBox="0 0 12 12"><rect x="1" y="2" width="10" height="8" fill="#888"/><path d="M1 2l5 4 5-4" stroke="#fff" fill="none"/></svg><a>info@brightoakfm.org.uk</a></li>
        <li><svg width="12" height="12" viewBox="0 0 12 12"><path d="M6 11S2 7 2 4.5a4 4 0 0 1 8 0C10 7 6 11 6 11z" fill="#888"/></svg>4123 lorem Ipsum Dummy Lorem Ipsum</li>
      </ul>
    </div>
    <div class="foot-col links">
      <h4>Quick Links</h4>
      <ul><li>Home</li><li>About us</li><li>Services</li><li>Training</li><li>Contact us</li></ul>
    </div>
    <div class="foot-col follow">
      <h4>Follow Us</h4>
      <p>Lorem ipsum dolor sit amet, conse ctetur adipiscing elit. Nulla in purus nibh. Donec ornare</p>
      <div class="socials"><span></span><span></span><span></span><span></span><span></span></div>
    </div>
  </div>
</footer>
<div class="bottom-bar">© Copyright 2016 Bright Oak FM.All Rights Reserved</div>

</body>
</html>
```